Hip surgeon needs a stationery design

I need a new stationery design for my private practice.
My practice is focused in hip arthroplasty (hip prosthesis).
I'd like to see designs most in blue or shades of blue.
I've uploaded my new logo to help with the task.
Also, I'm a member of some societies and I've uploaded their logos either, so I'd like to see them in some of the stationeries.
Itens list:
business card
letterhead A4
envelope
prescription block A5
one fold for A4 (please see the archive "pocket")
Personal data:
Dr. Renan L. Vasconti
CRM/PR 57316
site: www.clinicapelvora.com.br
email: dr.renan@clinicapelvora.com.br
Adress:
Rua Leopoldo Marques Vieira de Lima, 712
Campo Sereno - Curitiba/PR
41 30875316 I 30875317
Updates
I forgot to mention that my practice is focused primarily in hip arthroplasty (total hip prosthesis) and the target audience range from young adults to the elderly.
I also perform hip preserving surgeries (open and arthroscopic procedures) and pelvic and hip fracture surgery (trauma).
- Any "cleaner" fonts are welcome

```html
<!DOCTYPE html>
<html lang="pt-BR">
<head>
<meta charset="utf-8">
<title>Stationery Design – Dr. Renan L. Vasconti</title>
<link rel="stylesheet" href="https://fonts.googleapis.com/css2?family=Roboto+Condensed:wght@400;700&family=Roboto:wght@400;500&family=Source+Sans+3:wght@400&display=swap">
<style>
  :root {
    --board: #8c8c8c;
    --paper: #ffffff;
    --blue: #1b7dc3;
    --blue-light: #2aa3dc;
    --ink: #333333;
    --rule: #9a9a9a;
    --ghost: #ececec;
    --caption: #eeeeee;
    --shadow: 2px 2px 4px rgba(0, 0, 0, .45);
  }
  * { box-sizing: border-box; margin: 0; padding: 0; }
  html, body { width: 1200px; height: 640px; overflow: hidden; background: var(--board); }
  .board { position: relative; width: 1200px; height: 640px; background: var(--board); font-family: "Roboto", Arial, sans-serif; }
  .sheet { position: absolute; background: var(--paper); box-shadow: var(--shadow); overflow: hidden; }
  .sheet--blue { background: var(--blue); }
  .mark { position: absolute; border-radius: 50%; background: var(--blue); }
  .mark--white { background: var(--paper); }
  .name { position: absolute; font-family: "Roboto Condensed", Arial, sans-serif; font-weight: 400; color: var(--blue); white-space: nowrap; line-height: 1; }
  .tagline { position: absolute; font-family: "Roboto Condensed", Arial, sans-serif; color: var(--blue); white-space: nowrap; line-height: 1; }
  .on-blue { color: var(--paper); }
  .rule { position: absolute; height: 1.5px; background: var(--blue); }
  .contact-row { position: absolute; display: flex; gap: 7px; font-size: 5px; color: var(--ink); white-space: nowrap; align-items: center; }
  .contact-row span, .contact-list li { display: flex; align-items: center; gap: 3px; }
  .icon { width: 6px; height: 6px; flex: none; }
  .contact-list { position: absolute; list-style: none; font-size: 5.4px; color: var(--ink); white-space: nowrap; line-height: 7.6px; }
  .contact-list.on-blue { color: var(--paper); }
  .card-title { position: absolute; right: 16px; text-align: right; font-family: "Roboto Condensed", Arial, sans-serif; }
  .card-title strong { display: block; font-size: 8.6px; font-weight: 700; }
  .card-title small { display: block; font-size: 4.8px; color: var(--ink); margin-top: 2px; }
  .ghost { position: absolute; border-radius: 50%; background: var(--ghost); }
  .flap { position: absolute; left: 0; top: 0; }
  .caption { position: absolute; left: 985px; top: 518px; color: var(--caption); font-family: "Source Sans 3", Arial, sans-serif; font-size: 13px; line-height: 16.6px; }
  .caption h1 { font-size: 18px; font-weight: 400; line-height: 22px; }
  .caption ul { list-style: none; }
</style>
</head>
<body>
<svg width="0" height="0" style="position:absolute" aria-hidden="true">
  <symbol id="i-phone" viewBox="0 0 10 10"><rect x="3" y="1" width="4" height="8" rx=".8" fill="currentColor"/></symbol>
  <symbol id="i-tel" viewBox="0 0 10 10"><path d="M1 4c0-2 8-2 8 0v1H7V4H3v1H1zM2 6h6v3H2z" fill="currentColor"/></symbol>
  <symbol id="i-mail" viewBox="0 0 10 10"><rect x="1" y="2.5" width="8" height="5" rx=".8" fill="currentColor"/></symbol>
  <symbol id="i-web" viewBox="0 0 10 10"><circle cx="5" cy="5" r="3.6" fill="none" stroke="currentColor" stroke-width="1.4"/><path d="M1.5 5h7" stroke="currentColor"/></symbol>
  <symbol id="i-pin" viewBox="0 0 10 10"><path d="M5 9.5 2 5.2A3.3 3.3 0 1 1 8 5.2z" fill="currentColor"/></symbol>
</svg>

<main class="board">

  <!-- Letterhead -->
  <section class="sheet letterhead" style="left:22px;top:30px;width:416px;height:536px;">
    <div class="ghost" role="img" aria-label="Faint brand circle" style="left:-40px;top:350px;width:210px;height:210px;"></div>
    <div class="mark" style="left:30px;top:23px;width:40px;height:40px;"></div>
    <div class="name" style="left:73px;top:25px;font-size:19px;">Dr. Renan L. Vasconti</div>
    <div class="tagline" style="left:73px;top:47px;font-size:12.5px;">Cirurgia do Quadril</div>
    <div class="contact-row" style="right:12px;top:47px;">
      <span><svg class="icon" style="color:var(--blue)"><use href="#i-mail"/></svg>dr.renan@clinicapelvora.com.br</span>
      <span><svg class="icon" style="color:var(--blue-light)"><use href="#i-pin"/></svg>Rua Leopoldo M. V. de Lima, 712</span>
    </div>
    <div class="rule" style="left:188px;right:0;top:55px;"></div>
  </section>

  <!-- Business card front, blue -->
  <section class="sheet sheet--blue card" style="left:457px;top:26px;width:220px;height:128px;">
    <div class="mark mark--white" style="left:-45px;top:34px;width:130px;height:130px;"></div>
    <div class="card-title on-blue" style="top:16px;"><strong>Dr. Renan L. Vasconti</strong><small class="on-blue">Managing Director</small></div>
    <ul class="contact-list on-blue" style="left:114px;top:76px;">
      <li><svg class="icon"><use href="#i-phone"/></svg>41 30875316</li>
      <li><svg class="icon"><use href="#i-tel"/></svg>41 30875317</li>
      <li><svg class="icon"><use href="#i-mail"/></svg>dr.renan@clinicapelvora.com.br</li>
      <li><svg class="icon"><use href="#i-web"/></svg>www.clinicapelvora.com.br</li>
      <li><svg class="icon"><use href="#i-pin"/></svg>Rua Leopoldo M. V. de Lima, 712</li>
    </ul>
  </section>

  <!-- Business card back, blue -->
  <section class="sheet sheet--blue card" style="left:703px;top:26px;width:220px;height:128px;">
    <div class="mark mark--white" style="left:21px;top:46px;width:36px;height:36px;"></div>
    <div class="name on-blue" style="left:63px;top:48px;font-size:16px;">Dr. Renan L. Vasconti</div>
    <div class="tagline on-blue" style="left:63px;top:66px;font-size:11.5px;">Cirurgia do Quadril</div>
  </section>

  <!-- Business card front, white -->
  <section class="sheet card" style="left:946px;top:26px;width:226px;height:132px;">
    <div class="mark" style="left:-40px;top:36px;width:130px;height:130px;"></div>
    <div class="card-title" style="top:16px;color:var(--blue);"><strong>Dr. Renan L. Vasconti</strong><small>Managing Director</small></div>
    <ul class="contact-list" style="left:113px;top:76px;">
      <li><svg class="icon" style="color:var(--blue)"><use href="#i-phone"/></svg>41 30875316</li>
      <li><svg class="icon" style="color:var(--blue)"><use href="#i-tel"/></svg>41 30875317</li>
      <li><svg class="icon" style="color:var(--blue)"><use href="#i-mail"/></svg>dr.renan@clinicapelvora.com.br</li>
      <li><svg class="icon" style="color:var(--blue)"><use href="#i-web"/></svg>www.clinicapelvora.com.br</li>
      <li><svg class="icon" style="color:var(--blue)"><use href="#i-pin"/></svg>Rua Leopoldo M. V. de Lima, 712</li>
    </ul>
  </section>

  <!-- Envelope front -->
  <section class="sheet envelope" style="left:455px;top:180px;width:458px;height:210px;">
    <div class="mark" style="left:17px;top:152px;width:44px;height:44px;"></div>
    <div class="name" style="left:66px;top:155px;font-size:19.5px;">Dr. Renan L. Vasconti</div>
    <div class="tagline" style="left:66px;top:178px;font-size:13px;">Cirurgia do Quadril</div>
    <div class="contact-row" style="right:30px;top:178px;">
      <span><svg class="icon" style="color:var(--blue)"><use href="#i-mail"/></svg>dr.renan@clinicapelvora.com.br</span>
      <span><svg class="icon" style="color:var(--blue-light)"><use href="#i-pin"/></svg>Rua Leopoldo M. V. de Lima, 712</span>
    </div>
    <div class="rule" style="left:198px;right:0;top:188px;"></div>
  </section>

  <!-- Business card, white layout two -->
  <section class="sheet card" style="left:948px;top:180px;width:222px;height:130px;">
    <div class="mark" style="left:16px;top:14px;width:24px;height:24px;"></div>
    <div class="name" style="left:42px;top:15px;font-size:11px;">Dr. Renan L. Vasconti</div>
    <div class="tagline" style="left:42px;top:28px;font-size:8px;">Cirurgia do Quadril</div>
    <div class="card-title" style="top:48px;right:14px;color:var(--blue);"><strong>Dr. Renan L. Vasconti</strong><small>Managing Director</small></div>
    <div class="rule" style="left:16px;right:50px;top:61px;height:1px;background:var(--rule);"></div>
    <ul class="contact-list" style="left:16px;top:71px;line-height:9.5px;">
      <li><svg class="icon" style="color:var(--blue-light)"><use href="#i-phone"/></svg>41 30875316</li>
      <li><svg class="icon" style="color:var(--blue-light)"><use href="#i-tel"/></svg>41 30875317</li>
      <li><svg class="icon" style="color:var(--blue-light)"><use href="#i-mail"/></svg>dr.renan@clinicapelvora.com.br</li>
      <li><svg class="icon" style="color:var(--blue-light)"><use href="#i-web"/></svg>www.clinicapelvora.com.br</li>
      <li><svg class="icon" style="color:var(--blue-light)"><use href="#i-pin"/></svg>Rua Leopoldo M. V. de Lima, 712</li>
    </ul>
  </section>

  <!-- Envelope back -->
  <section class="sheet envelope-back" style="left:457px;top:411px;width:457px;height:210px;">
    <svg class="flap" width="457" height="70" viewBox="0 0 457 70" aria-hidden="true">
      <path d="M2 0 V48 Q2 62 20 62 H437 Q455 62 455 48 V0" fill="none" stroke="var(--rule)" stroke-width="1"/>
    </svg>
    <div class="mark" style="left:205px;top:10px;width:47px;height:47px;"></div>
  </section>

  <!-- Business card back, white -->
  <section class="sheet card" style="left:948px;top:335px;width:224px;height:131px;">
    <div class="mark" style="left:22px;top:44px;width:39px;height:39px;"></div>
    <div class="name" style="left:64px;top:47px;font-size:16.5px;">Dr. Renan L. Vasconti</div>
    <div class="tagline" style="left:64px;top:66px;font-size:11.5px;">Cirurgia do Quadril</div>
  </section>

  <aside class="caption">
    <h1>Stationery Design</h1>
    <ul>
      <li>Business Card front</li>
      <li>Business Card Back</li>
      <li>Letterhead</li>
      <li>Envelope Front</li>
      <li>Envelope Back</li>
    </ul>
  </aside>

</main>
</body>
</html>
```